Stationary for New Company

We need stationary designed for a new company. Details of the required stationary is attached.

The final version should be trendy, clean... only 2 colours (green + grey/black) and professional.

#1: Business Cards (design on 2 sides)
#2: Letterhead (word format)
#3: Cover Page and back cover for proposals
#4: Envelopes,
#5: Thank You card,
#6: Presentation Folder,
#7: Email signatures template (sample attached in word document)

Logo is attached. Logo can be reversed out (will attach once available). Logo can be stacked or horizontal (provided as horizontal).

Files need to be provided in ai + png format.

Target Market(s)

Business owners. More affluent.

Industry/Entity Type

Business

Requirements
Must have
• See brief

Font: Calibri
Should not have
• Photographs / stock photos

```html
<!DOCTYPE html>
<html lang="en">
<head>
<meta charset="utf-8">
<title>Northgate Insurance Brokers – Envelope</title>
<link rel="stylesheet" href="https://fonts.googleapis.com/css2?family=Carlito:wght@400;700&display=swap">
<style>
  :root {
    --brand-green: #6a9139;
    --brand-grey: #858688;
    --ink: #1e1e1e;
    --paper: #ffffff;
  }
  * { margin: 0; padding: 0; box-sizing: border-box; }
  html, body {
    width: 1200px;
    height: 524px;
    overflow: hidden;
    background: var(--paper);
  }
  .envelope {
    position: relative;
    width: 1200px;
    height: 524px;
    background: var(--paper);
    font-family: "Carlito", "Calibri", sans-serif;
  }
  .band { position: absolute; left: 0; width: 100%; }
  .band--top-accent { top: 0; height: 6px; background: var(--brand-green); }
  .band--top { top: 6px; height: 23px; background: var(--brand-grey); }
  .band--bottom-accent { top: 482px; height: 11px; background: var(--brand-green); }
  .band--bottom { top: 493px; height: 31px; background: var(--brand-grey); }

  .brand {
    position: absolute;
    top: 43px;
    left: 17px;
    display: flex;
    align-items: center;
    gap: 16px;
  }
  .brand__square {
    width: 79px;
    height: 88px;
    background: var(--brand-green);
  }
  .brand__name {
    color: var(--brand-grey);
    font-weight: 400;
    font-size: 38px;
    line-height: 1.05;
    letter-spacing: 0.2px;
  }

  .contact {
    position: absolute;
    top: 421px;
    left: 0;
    width: 100%;
    text-align: center;
    font-size: 11.5px;
    line-height: 16px;
    color: var(--ink);
  }
  .contact__label { color: var(--brand-green); margin-right: 4px; }
  .contact__item + .contact__item { margin-left: 6px; }
</style>
</head>
<body>
  <main class="envelope">
    <div class="band band--top-accent"></div>
    <div class="band band--top"></div>

    <header class="brand">
      <div class="brand__square"></div>
      <div class="brand__name">Northgate<br>Insurance Brokers</div>
    </header>

    <footer class="contact">
      <p><span class="contact__label">Website:</span> www.northgateinsurance.com</p>
      <p>2250 Maple Ridge Road NW Calgary, AB&nbsp; T3A 5K8</p>
      <p>
        <span class="contact__item"><span class="contact__label">Phone:</span> 555.210.4400</span>
        <span class="contact__item"><span class="contact__label">Fax:</span> 555.210.4401</span>
        <span class="contact__item"><span class="contact__label">Toll Free:</span> 800.555.0199</span>
      </p>
    </footer>

    <div class="band band--bottom-accent"></div>
    <div class="band band--bottom"></div>
  </main>
</body>
</html>
```